MARVELTRUST web-presence redisign

We would like to have our existing web-presence redesigned. Have a look at www.pelbrika-example.ch (please use explorer). To the existing 11 pages we would add one more.

```html
<!DOCTYPE html>
<html lang="de">
<head>
<meta charset="utf-8">
<title>MARVELTRUST Zaharztpraxis</title>
<link href="https://fonts.googleapis.com/css2?family=Arimo:wght@400;700&display=swap" rel="stylesheet">
<style>
:root{
  --brand:#1fb6e0;
  --card-blue:#3fb0d4;
  --text:#3a3a3a;
  --muted:#555;
  --grey-title:#9a9a9a;
  --line:#cfcfcf;
  --footer:#5b5b5b;
  --white:#fff;
}
*{margin:0;padding:0;box-sizing:border-box}
html,body{width:1000px;height:1200px;overflow:hidden}
body{font-family:Arimo,Arial,sans-serif;color:var(--text);background:var(--white);position:relative}
.hero{position:absolute;left:0;top:0;width:1000px;height:363px;
  background:radial-gradient(ellipse at 45% 20%,#d8f6fc 0%,#8fdcef 35%,#2fb1d9 75%,#1899c8 100%)}
.logo{position:absolute;left:207px;top:44px;line-height:1;width:170px}
.logo .name{font-weight:700;font-size:22px;color:var(--brand);letter-spacing:-.3px;white-space:nowrap}
.logo .sub{font-size:18px;color:#4a4a4a;letter-spacing:1px;margin-top:3px}
.social{position:absolute;top:17px;left:725px;display:flex;gap:6px}
.social span{width:18px;height:18px;background:#1f5fa8;border-radius:2px;display:block}
.nav{position:absolute;left:388px;top:43px;width:404px;height:43px;background:rgba(255,255,255,.85);
  display:flex;align-items:center;justify-content:center;gap:10px;font-size:10px;color:#555}
.nav a{color:#555;text-decoration:none}
.nav a.active{color:#222;font-weight:700;text-decoration:underline}
.nav i{font-style:normal;font-size:8px;color:#777}
.hero-text{position:absolute;left:207px;top:135px;color:var(--white);width:230px}
.hero-text h1{font-size:28px;line-height:29px;font-weight:700;letter-spacing:-.5px;white-space:nowrap}
.hero-text h2{font-size:18px;line-height:19px;font-weight:400;color:#1a1a1a;margin-top:10px;white-space:nowrap}
.hero-text p{font-size:8px;line-height:13px;margin-top:10px;width:212px}
.hero-photo{position:absolute;left:440px;top:90px;width:400px;height:273px;
  background:radial-gradient(ellipse at 65% 55%,#f4f4f4 0%,#e2eef2 45%,rgba(200,235,245,0) 75%)}
.arrow{position:absolute;top:203px;width:43px;height:43px;border:2px solid var(--white);border-radius:50%}
.arrow svg{display:block}
.dots{position:absolute;left:476px;top:337px;display:flex;gap:11px}
.dots span{width:8px;height:8px;border-radius:50%;background:var(--white)}
.dots span.on{background:#111}
.cards{position:absolute;top:388px;left:207px;display:flex;gap:31px}
.card{width:123px;height:210px;border:1px solid var(--line);text-align:center;padding-top:17px;background:var(--white)}
.card.active{background:var(--card-blue);border-color:var(--card-blue);box-shadow:0 2px 5px rgba(0,0,0,.3)}
.card .ico{width:52px;height:52px;margin:0 auto;background:#8c8c8c;border-radius:4px;display:flex;align-items:center;justify-content:center}
.card.active .ico{background:none;border:2px solid var(--white);border-radius:6px}
.card h3{font-size:12.5px;margin-top:17px;color:var(--grey-title)}
.card.active h3,.card.active p{color:var(--white)}
.card p{font-size:8px;line-height:14.4px;margin-top:12px;color:var(--muted);padding:0 7px}
.welcome{position:absolute;left:214px;top:623px;width:355px}
.welcome h2{font-size:12.5px;font-weight:700;color:#333}
.welcome p{font-size:7.8px;line-height:14px;color:var(--muted);margin-top:9px}
.divider-h{position:absolute;left:208px;top:742px;width:365px;height:1px;background:#ddd}
.divider-v{position:absolute;left:588px;top:624px;width:1px;height:270px;background:#ddd}
.team{position:absolute;left:214px;top:752px;width:348px}
.team h2{font-size:12.5px;color:#333}
.team .bar{height:4px;background:#eee;margin-top:7px;position:relative}
.team .bar::before{content:"";position:absolute;left:0;top:0;width:37px;height:4px;background:#555}
.doctors{display:flex;gap:32px;margin-top:14px}
.doc{width:57px;font-size:7.8px;line-height:10px;color:#555}
.doc .ph{width:57px;height:57px;background:linear-gradient(#c9a48a,#e6c9b4);box-shadow:0 1px 3px rgba(0,0,0,.3);border:2px solid #fff;margin-bottom:6px}
.news{position:absolute;left:606px;top:623px;width:185px}
.news h2{font-size:12.5px;color:#333}
.news h4{font-size:10px;font-weight:400;color:#444;margin-top:14px}
.news .img{width:185px;height:59px;margin-top:4px}
.news p{font-size:7.4px;line-height:9.5px;color:#444;margin-top:5px}
.footer{position:absolute;left:0;top:916px;width:1000px;height:233px;background:var(--footer);color:var(--white)}
.footer .map{position:absolute;left:330px;top:0;width:520px;height:233px;
  background:radial-gradient(ellipse at 50% 40%,#6e6e6e 0%,#626262 55%,rgba(91,91,91,0) 80%)}
.footer .logo{top:50px}
.footer .logo .name{color:var(--white);font-size:24px}
.footer .logo .sub{color:var(--white)}
.contact{position:absolute;left:207px;top:119px;font-size:10px;letter-spacing:.6px;line-height:25px}
.contact div{display:flex;align-items:center;gap:10px}
.links{position:absolute;font-size:10px;letter-spacing:.6px;display:flex;align-items:center;gap:6px}
.links svg{display:block}
.copy{position:absolute;left:0;top:1162px;width:1000px;text-align:center;font-size:9.5px;line-height:14px;color:#222}
</style>
</head>
<body>
<header class="hero">
  <div class="hero-photo" role="img" aria-label="Photo of a smiling dentist in a white coat holding a green apple"></div>
  <div class="logo"><div class="name">MARVELTRUST</div><div class="sub">Zaharztpraxis</div></div>
  <div class="social"><span></span><span></span><span></span></div>
  <nav class="nav">
    <a class="active" href="#">Home</a><i>•</i><a href="#">Zahnmedizin</a><i>•</i><a href="#">Dentalhygiene</a><i>•</i><a href="#">Team</a><i>•</i><a href="#">Contact us</a>
  </nav>
  <div class="hero-text">
    <h1>Smile &amp; Shine<br>Like a Celebrity</h1>
    <h2>with a simple and safe<br>20 minute treatment</h2>
    <p>Lorem Ipsum is simply dummy text of the printing and typesetting industry. Lorem Ipsum has been the industry's standard dummy text ever since the 1500s, when an unknown printer took a galley of type and scrambled it to make a type specimen book.</p>
  </div>
  <div class="arrow" style="left:85px"><svg width="39" height="39"><path d="M23 10 L14 19.5 L23 29" fill="none" stroke="#fff" stroke-width="2"/></svg></div>
  <div class="arrow" style="left:872px"><svg width="39" height="39"><path d="M16 10 L25 19.5 L16 29" fill="none" stroke="#fff" stroke-width="2"/></svg></div>
  <div class="dots"><span></span><span class="on"></span><span></span></div>
</header>

<section class="cards">
  <div class="card active"><div class="ico"><svg width="30" height="30"><path d="M11 2h8v9h9v8h-9v9h-8v-9H2v-8h9z" fill="#fff"/></svg></div><h3>01 Emergency</h3><p>In convallis venenatis magna, nec interdum ipsum iaculis et. Nulla facilisi. Duis in neque malesuada vestibulum ut neque.</p></div>
  <div class="card"><div class="ico"><svg width="30" height="30"><rect x="3" y="8" width="24" height="18" rx="2" fill="#fff"/><rect x="11" y="4" width="8" height="5" fill="none" stroke="#fff" stroke-width="2"/><circle cx="15" cy="17" r="5" fill="#8c8c8c"/><path d="M13.5 14h3v1.5H18v3h-1.5V20h-3v-1.5H12v-3h1.5z" fill="#fff"/></svg></div><h3>02 New Services</h3><p>In convallis venenatis magna, nec interdum ipsum iaculis et. Nulla facilisi. Duis in neque malesuada vestibulum ut neque.</p></div>
  <div class="card"><div class="ico"><svg width="30" height="30"><path d="M7 3v9a7 7 0 0 0 14 0V3M14 19v3a4 4 0 0 0 8 0v-2" fill="none" stroke="#fff" stroke-width="2"/><circle cx="22" cy="18" r="2.5" fill="none" stroke="#fff" stroke-width="1.5"/></svg></div><h3>03 Our Advice</h3><p>In convallis venenatis magna, nec interdum ipsum iaculis et. Nulla facilisi. Duis in neque malesuada vestibulum ut neque.</p></div>
  <div class="card"><div class="ico"><svg width="30" height="30"><path d="M15 3v25" stroke="#fff" stroke-width="2"/><path d="M3 9q6 4 12 0q6 4 12 0" fill="none" stroke="#fff" stroke-width="2"/><path d="M11 14q8 2 0 5q8 2 0 5" fill="none" stroke="#fff" stroke-width="1.5"/><circle cx="15" cy="4" r="2" fill="#fff"/></svg></div><h3>04 On-Line Help</h3><p>In convallis venenatis magna, nec interdum ipsum iaculis et. Nulla facilisi. Duis in neque malesuada vestibulum ut neque.</p></div>
</section>

<section class="welcome">
  <h2>Herzlich willkommen in unserer neuen Praxis.</h2>
  <p>Es ist unser Ziel, Ihr Wohlbefinden zu steigern. Sie sollen die Schönheit des Alltags mit gesunden Zähnen geniessen und in jeder Situation herzhaft lachen können.</p>
  <p>Ihre Zahnärztin</p>
  <p>Dr. med. dent. Lena Marwald-Keller</p>
</section>
<div class="divider-h"></div>
<div class="divider-v"></div>

<section class="team">
  <h2>Meet Our Doctor 1</h2>
  <div class="bar"></div>
  <div class="doctors">
    <div class="doc"><div class="ph" role="img" aria-label="Portrait photo of Dr. Lena"></div>Dr. med. dent.<br>Lena</div>
    <div class="doc"><div class="ph" role="img" aria-label="Portrait photo of Dr. Mira Hollenstein"></div>Dr. med. dent.<br>Mira Hollenstein<br>Zahnärztin</div>
    <div class="doc"><div class="ph" role="img" aria-label="Portrait photo of Selin Arkan"></div>Selin Arkan<br>Dentalhygienikerin</div>
    <div class="doc"><div class="ph" role="img" aria-label="Portrait photo of Anouk Brändli"></div>Anouk Brändli<br>Dentalhygienikerin</div>
  </div>
</section>

<aside class="news">
  <h2>Lastest News</h2>
  <h4>Hospital</h4>
  <div class="img" role="img" aria-label="Close-up photo of white teeth" style="background:linear-gradient(90deg,#8a2a22,#e9e2d8 40%,#c98a80 80%,#5a1a16)"></div>
  <p>"Life is a series of impressions both good and bad. A healthy smile and the condition of your teeth says a lot about who you are."</p>
  <h4>How to Brush</h4>
  <div class="img" role="img" aria-label="Photo of a toothbrush on a denture model" style="background:linear-gradient(90deg,#3a64c8,#e7b0a8 45%,#f0dcd5 80%,#eee)"></div>
  <p>"Life is a series of impressions both good and bad. A healthy smile and the condition of your teeth says a lot about who you are."</p>
</aside>

<footer class="footer">
  <div class="map" role="img" aria-label="Dotted world map with location rings marking the practice"></div>
  <div class="logo"><div class="name">MARVELTRUST</div><div class="sub">Zaharztpraxis</div></div>
  <div class="contact">
    <div><svg width="13" height="12"><path d="M6.5 0L13 6h-2v6H8V8H5v4H2V6H0z" fill="#fff"/></svg>Seefeldweg 12 CH-8600 Musterdorf</div>
    <div><svg width="13" height="12"><rect x="3" y="0" width="7" height="12" rx="1" fill="none" stroke="#fff" stroke-width="1.5"/></svg>T: +41 (0)44 555 01 23</div>
    <div><svg width="13" height="12"><rect x="2" y="2" width="11" height="8" fill="none" stroke="#fff"/><path d="M2 2l5.5 4 5.5-4" fill="none" stroke="#fff"/></svg>info@pelbrika-example.ch</div>
  </div>
  <div class="links" style="left:631px;top:55px"><svg width="11" height="11"><circle cx="5.5" cy="5.5" r="5.5" fill="#fff"/><path d="M4.5 3l2.5 2.5-2.5 2.5" fill="none" stroke="#5b5b5b" stroke-width="1.3"/></svg>Contact Form</div>
  <div class="links" style="left:662px;top:113px"><svg width="11" height="11"><circle cx="5.5" cy="5.5" r="5.5" fill="#fff"/><path d="M4.5 3l2.5 2.5-2.5 2.5" fill="none" stroke="#5b5b5b" stroke-width="1.3"/></svg>Zoom in the map</div>
  <div class="links" style="left:624px;top:163px"><svg width="11" height="11"><circle cx="5.5" cy="5.5" r="5.5" fill="#fff"/><path d="M4.5 3l2.5 2.5-2.5 2.5" fill="none" stroke="#5b5b5b" stroke-width="1.3"/></svg>Meet our team</div>
</footer>

<div class="copy">Copyright 2014 © MARVELTRUST | Dr. med. dent. L. Marwald-Keller.<br>All rights reserved. Privacy Policy</div>
</body>
</html>
```